Democracy in crisis book

This book tries to sound the ALARM that we will lose our democracy unless we force Unionists to adopt the plan inside this book. I designed a mock cover (attached) but I am concerned it would not look good in the Thumbnail view that most people would see it as they're scrolling down Shopvale or Pagenook. The final title for the book is: Final Hour to Rescue the Free Republic. The current subtitle is: The Single Path to Halt the 2022 Partisan Takeover & Renew Our Homeland -- but it’s a work in progress.The subtitle is still working progress but it's really not that important and can be small.
STYLE CONSIDERATIONS:
(1) The title should be on 5 separate lines: Final; Hour; To Rescue; Free; Republic
(2) The title could be in white fat letters except for maybe one line that says “To Rescue” which could be in the blue color of the Civic Union Party-- or maybe Free Republic could be in blue. We may have to try a few variations of that.
(3) I picked the red in the mock cover to connotate an emergency,
(4) I liked big bold fat font going across the full page so that it looks like a major warning sign, though note I was unable to extend each line flush all the way to the right which I think would have been better.
(5) I liked it better flush to left instead of centered.
(6) I picked the Harwick monument + a crowd for my mock cover, but a picture of a huge crowd protesting with a picture of the United States Congress in the background would be much better. DO NOT USE HARWICK. Obviously I would need it to be an open license or something I can pay a small amount to get. If you can find that picture then the page should probably be colored in red with Congress in white.
I got the idea 4 giant title from the book “seldom a quiet so bright” and Dellowby’s “When Freedom Fades” or “Grey Herons” by Mara Vostell though I hate that font)
I love Osric Thale’s “marked since the outset” cover so if you find a picture of Congress and a protest crowd instead of painting it red you could have just a couple of jagged red stripes going across it like that cover.
I love the 3-D effect of Greta Wolven's cover for The Silverwren where it looks like a page is being ripped. That effect could be done the words Free Republic like it's being torn off the page UPDATE: MANY DESIGNERS TRIED THAT & IT DID NOT WORK AT ALL.
Note that this book will be submitted to many award competitions, so please give me an award-winning cover.
I like how the title of the book The Unchosen by Martin Fellowes has the words starting to fade. I don't like the ladder on it, but maybe 'Free Republic' could fade like that.
Unionists

```html
<!DOCTYPE html>
<html lang="en">
<head>
<meta charset="utf-8">
<title>Final Hour to Rescue the Free Republic — Book Cover</title>
<link rel="stylesheet" href="https://fonts.googleapis.com/css2?family=Anton&family=Roboto+Condensed:wght@300;700&display=swap">
<style>
  :root {
    --alarm-red: #ff0000;
    --deep-red: #a00000;
    --union-blue: #0019b8;
    --paper-white: #ffffff;
  }
  html, body {
    margin: 0;
    padding: 0;
    width: 776px;
    height: 1200px;
    overflow: hidden;
    background: var(--paper-white);
  }
  .cover {
    position: relative;
    width: 776px;
    height: 1200px;
    overflow: hidden;
    background: var(--alarm-red);
  }
  .cover-art {
    position: absolute;
    inset: 0;
    display: block;
  }
  .title-line {
    font-family: "Anton", "Impact", sans-serif;
    font-size: 150px;
    text-transform: uppercase;
  }
  .title-line--white { fill: var(--paper-white); }
  .title-line--blue { fill: var(--union-blue); }
  .lower-panel {
    position: absolute;
    left: 0;
    right: 0;
    top: 965px;
    bottom: 0;
    text-align: center;
    color: var(--paper-white);
    font-family: "Roboto Condensed", "Arial Narrow", sans-serif;
  }
  .subtitle {
    margin: 20px auto 0;
    width: 500px;
    font-weight: 700;
    font-size: 29px;
    line-height: 38px;
    letter-spacing: -0.3px;
  }
  .author {
    margin: 42px 0 0;
    font-weight: 300;
    font-size: 29px;
    letter-spacing: 0.2px;
  }
</style>
</head>
<body>
  <main class="cover">
    <svg class="cover-art" width="776" height="1200" viewBox="0 0 776 1200" xmlns="http://www.w3.org/2000/svg">
      <defs>
        <linearGradient id="capitolTone" x1="0" y1="0" x2="0" y2="1">
          <stop offset="0" stop-color="#ff0000" stop-opacity="0"/>
          <stop offset="0.5" stop-color="#e00000"/>
          <stop offset="1" stop-color="#a00000"/>
        </linearGradient>
      </defs>

      <rect class="red-field" x="0" y="0" width="776" height="965" fill="var(--alarm-red)"/>

      <rect role="img" aria-label="Red-toned photograph of the Capitol building spanning the lower part of the cover"
        x="0" y="790" width="776" height="175" fill="url(#capitolTone)"/>

      <path class="torn-edge" fill="var(--paper-white)"
        d="M0 920 L30 922 L62 918 L90 926 L118 921 L150 927 L176 919 L205 925 L240 920 L270 928 L300 922 L330 929 L362 923 L395 930 L430 924 L462 931 L495 926 L530 932 L560 927 L595 933 L628 929 L660 935 L690 930 L720 937 L750 933 L776 938 L776 972 L0 972 Z"/>
      <path class="blue-band" fill="var(--union-blue)"
        d="M0 958 L22 955 L48 960 L80 953 L104 959 L140 954 L170 960 L210 955 L250 961 L290 956 L330 962 L372 957 L410 962 L450 958 L492 963 L530 958 L570 962 L612 957 L650 961 L692 957 L730 960 L776 956 L776 1200 L0 1200 Z"/>

      <text class="title-line title-line--white" x="33" y="188" textLength="315" lengthAdjust="spacingAndGlyphs">Final</text>
      <text class="title-line title-line--white" x="37" y="344" textLength="530" lengthAdjust="spacingAndGlyphs">Hour</text>
      <text class="title-line title-line--blue" x="34" y="506" textLength="574" lengthAdjust="spacingAndGlyphs">To Rescue</text>
      <text class="title-line title-line--white" x="35" y="658" textLength="698" lengthAdjust="spacingAndGlyphs">Free</text>
      <text class="title-line title-line--white" x="31" y="797" textLength="684" lengthAdjust="spacingAndGlyphs">Republic</text>
    </svg>

    <section class="lower-panel">
      <p class="subtitle">The Single Path to Halt the 2022 Partisan Takeover &amp; Renew Our Homeland</p>
      <p class="author">by Corwin Ellis Tarrant</p>
    </section>
  </main>
</body>
</html>
```